DRONE FLYERS.: : Presentation of the Vireo Rotorcraft Drone Division Vireo Rotorcraft has ...

- 1-Service to mining companies•Volumetric/Photogrammetry• Geophysical surveys•Mapping•Inspections-2- Visual and / or thermal inspections• Power lines•Pipelines/pipelines• Railroads-3- Services to municipalities•Planning• Various inspections• Civil security-4- Agricultural -55service•Multispectral•Mapping•Volumetric/Photogrammetry

```html
<!DOCTYPE html>
<html lang="fr">
<head>
<meta charset="utf-8">
<title>Vireo Rotorcraft – Division Drones</title>
<link href="https://fonts.googleapis.com/css2?family=Archivo+Black&family=Montserrat:wght@400;500;700&family=Roboto+Condensed:wght@400&display=swap" rel="stylesheet">
<style>
  :root{
    --bg:#e4e2de;
    --ink:#1d1d1d;
    --black:#000;
    --white:#fff;
    --muted:#555;
    --rule:#dcdcdc;
    --panel-grey:#f3f3f3;
    --chart:#5b8ff0;
    --chart-fill:#c9d9fb;
  }
  *{box-sizing:border-box;margin:0;padding:0}
  html,body{width:1200px;height:1200px;overflow:hidden;background:var(--bg)}
  body{font-family:"Montserrat",sans-serif;color:var(--ink)}
  .brochure{position:absolute;left:0;top:176px;width:1200px;height:848px;background:var(--white);box-shadow:0 4px 18px rgba(0,0,0,.25)}
  .panel{position:absolute;top:0;height:848px}
  .panel-cover{left:0;width:400px;background:var(--black);color:var(--white)}
  .panel-intro{left:400px;width:405px}
  .panel-survey{left:805px;width:395px;background:linear-gradient(90deg,#ececec 0,#fff 22px)}
  .abs{position:absolute}
  .photo{position:absolute}

  /* cover */
  .brand{position:absolute;left:56px;top:34px;display:flex;align-items:center;gap:16px}
  .brand-mark{width:62px;height:62px;border:2px solid var(--white);border-radius:50%;flex:none}
  .brand-name{font-family:"Montserrat",sans-serif;font-weight:500;font-size:22px;line-height:27px;color:var(--white)}
  .tag{position:absolute;font-family:"Archivo Black",sans-serif;color:var(--white);font-size:13px;line-height:1}
  .tag-lg{font-size:17px}
  .zoom{position:absolute;font-family:"Archivo Black",sans-serif;font-size:11px;color:#111;background:rgba(255,255,255,.85);padding:1px 3px}
  .phone{position:absolute;left:0;width:400px;top:766px;text-align:center;font-family:"Archivo Black",sans-serif;font-size:38px;color:var(--white);letter-spacing:.5px}
  .web{position:absolute;left:0;width:400px;top:810px;text-align:center;font-family:"Roboto Condensed",sans-serif;font-size:21px;color:#bbb}
  .web b{color:var(--white);font-family:"Archivo Black",sans-serif;font-weight:400;font-size:19px}

  /* text */
  .body-text{position:absolute;font-size:13.4px;line-height:17.3px;text-align:justify;hyphens:auto;-webkit-hyphens:auto}
  .heading{position:absolute;font-weight:700;font-size:19px;letter-spacing:.6px}

  /* volume card */
  .vol-card{position:absolute;left:25px;top:63px;width:157px;font-size:8px;line-height:1.25;color:#222}
  .vol-card .title{font-size:10.5px;font-weight:500;padding-bottom:8px;border-bottom:1px solid var(--rule)}
  .vol-card p{margin-top:7px}
  .vol-card p.tight{margin-top:1px}

  .measure{position:absolute;top:680px;width:92px;height:140px;background:var(--panel-grey);font-size:5.5px;color:#666;padding:4px 4px}
  .measure h4{font-size:7.5px;font-weight:700;color:#222;margin-bottom:6px}
  .measure .row{display:flex;justify-content:space-between;gap:3px;height:17px;align-items:center}
  .measure .row span:first-child{flex:1;min-width:0;line-height:1.1}
  .measure .row span:last-child{white-space:nowrap;flex:none}
  .measure .box{width:6px;height:6px;border:1px solid #888;display:inline-block}
  .measure .box.on{background:var(--chart);border-color:var(--chart)}
</style>
</head>
<body>
<div class="brochure">

  <section class="panel panel-cover">
    <div class="brand">
      <span class="brand-mark"></span>
      <span class="brand-name">Vireo Rotorcraft<br>Drone Division</span>
    </div>

    <div class="photo" role="img" aria-label="Drone en vol devant un hélicoptère jaune au sol" style="left:39px;top:131px;width:326px;height:95px;background:linear-gradient(180deg,#3d6fb8,#6f8fb0 60%,#8a7a4a)"></div>
    <div class="photo" role="img" aria-label="Image thermique d'une installation industrielle" style="left:39px;top:226px;width:180px;height:124px;background:linear-gradient(135deg,#6b6b6b,#7e3aa8 50%,#e0702a)"></div>
    <div class="photo" role="img" aria-label="Drone hexacoptère avec caméra" style="left:219px;top:226px;width:146px;height:124px;background:linear-gradient(180deg,#f4f4f4,#dcdcdc)"></div>
    <span class="tag tag-lg" style="left:56px;top:330px">Thermographie</span>

    <span class="tag" style="left:39px;top:364px">Photogrammétrie</span>
    <div class="photo" role="img" aria-label="Vue aérienne d'une mine à ciel ouvert" style="left:39px;top:381px;width:115px;height:88px;background:linear-gradient(135deg,#5f7a4f,#b6b6ac)"></div>
    <span class="tag" style="left:166px;top:397px">Volumétrie</span>
    <div class="photo" role="img" aria-label="Modèle volumétrique coloré d'un terrain" style="left:143px;top:414px;width:120px;height:90px;background:linear-gradient(135deg,#2fa36c,#22c4c0 60%,#1a8f8a)"></div>
    <span class="tag" style="left:303px;top:434px">3D</span>
    <div class="photo" role="img" aria-label="Modèle 3D en relief d'un site" style="left:252px;top:451px;width:113px;height:90px;background:linear-gradient(135deg,#f0f0f0,#9c9c9c)"></div>

    <span class="tag tag-lg" style="left:39px;top:546px">Inspection détaillée</span>
    <div class="photo" role="img" aria-label="Aire d'hélicoptères vue de loin" style="left:39px;top:567px;width:153px;height:85px;background:linear-gradient(180deg,#d6dbe0,#7a7f84)"></div>
    <div class="photo" role="img" aria-label="Gros plan sur un hélicoptère rouge" style="left:213px;top:567px;width:152px;height:85px;background:linear-gradient(180deg,#b8bcc0,#c9283c)"></div>
    <div class="photo" role="img" aria-label="Hélicoptère rouge au sol" style="left:39px;top:663px;width:153px;height:85px;background:linear-gradient(180deg,#c9ced3,#7b7f83)"></div>
    <div class="photo" role="img" aria-label="Détail mécanique du rotor" style="left:213px;top:663px;width:152px;height:85px;background:linear-gradient(135deg,#d8d8d8,#3a3a3a)"></div>
    <span class="zoom" style="left:42px;top:570px">1x</span>
    <span class="zoom" style="left:216px;top:570px">60x</span>
    <span class="zoom" style="left:42px;top:666px">30x</span>
    <span class="zoom" style="left:216px;top:666px">160x</span>

    <div class="phone">418 555-0192</div>
    <div class="web">www.<b>vireorotorcraft</b>.com</div>
  </section>

  <section class="panel panel-intro">
    <p class="body-text" style="left:27px;top:22px;width:352px">Nous offrons une multitude de services dans plusieurs secteurs. Tous nos pilotes ont obtenu leur certification avancée de Transports Canada et possèdent d'innombrables heures d'utilisation de drones (RPAS). La sécurité est notre priorité absolue dans toutes nos missions. Nous avons du matériel certifié par Transports Canada et pouvons voler dans un espace aérien de classe G (non contrôlé) et dans des espaces aériens de classe C, D, E et F (contrôlés), de jour comme de nuit. Nous pouvons fournir à nos clients des solutions rapides en matière de planification de mission et être prêts à voler quelques heures après leur appel.</p>
    <h2 class="heading" style="left:0;width:405px;text-align:center;top:292px">PHOTOGRAMÉTRI</h2>
    <div class="photo" role="img" aria-label="Orthophoto aérienne d'un site minier entouré de forêt" style="left:27px;top:330px;width:352px;height:270px;background:radial-gradient(ellipse at 55% 55%,#c9c7c0 0,#a6a59c 38%,#5f7348 62%,#3e5630 100%)"></div>
    <p class="body-text" style="left:27px;top:624px;width:352px">Nous pouvons obtenir des données d'inspections précises au centimètre près plus rapidement que les techniques d'inspection traditionnelles, ce qui permet d'enquêter sur des zones difficiles et / ou dangereuses pour l'homme. La photogrammétrie créent des « cartes photographiques » à partir de photographies aériennes ; La suppression de la distorsion et l'introduction de mesures précises sur des distances d'échantillonnage au sol permettent aux opérateurs de compiler des modèles numériques d'élévation, des contours, des mesures de volume, etc.</p>
  </section>

  <section class="panel panel-survey">
    <h2 class="heading" style="left:25px;top:27px">VOLUMÉTRIE</h2>
    <div class="vol-card">
      <div class="title">Volume Calculation</div>
      <p style="margin-top:24px">Calculated Volume: <b>1,565.86 yd³</b></p>
      <p style="margin-top:15px">Void Volume: <b>5,338.70 yd³</b></p>
      <p style="margin-top:15px">Minimum Height: <b>1,029.56 ft</b></p>
      <p class="tight">Maximum Height: <b>1,045.90 ft</b></p>
      <p class="tight">Area of Measurement: <b>1406.97 yd²</b></p>
    </div>
    <div class="photo" role="img" aria-label="Vue aérienne d'une pile de matériaux délimitée en orange" style="left:199px;top:63px;width:176px;height:134px;background:radial-gradient(ellipse at 55% 50%,#c9a06a 0,#a9a69d 30%,#8f918b 100%)"></div>

    <p class="body-text" style="left:25px;top:240px;width:350px">Le drone-arpentage est une alternative rapide, précise et économique au levé traditionnel. Une équipe d'enquêteurs a peut-être déjà eu à parcourir les bois, mais les technologies de drones modernes permettent l'utilisation d'enquêtes sur les systèmes d'information géographique (enquêtes SIG) permettant de capturer, d'analyser et de corréler des quantités de données recueillies à partir de plusieurs drones. L'utilisation de drones réduit considérablement le temps passé à collecter des données, et un seul vol peut générer des millions de points de données qu'il faudrait plusieurs semaines à une équipe humaine. Non seulement cette méthode est-elle beaucoup plus efficace et économique que les formes d'arpentage plus anciennes, mais les risques pour la sécurité liés à l'arpentage sont considérablement réduits - moins de temps sur le terrain signifie moins de risques pour les équipes d'arpenteurs dans les zones raides ou instables.</p>

    <h2 class="heading" style="left:24px;top:637px">PENTE &amp; COURBE DE NIVEAU</h2>

    <div class="measure" style="left:25px">
      <h4>Measurements</h4>
      <div class="row"><span>2D length</span><span>7.72 m</span></div>
      <div class="row"><span>3D length</span><span>7.72 m</span></div>
      <div class="row"><span>Min. elevation</span><span>675.27 m</span></div>
      <div class="row"><span>Max. elevation</span><span>675.27 m</span></div>
      <div class="row"><span>Elevation difference</span><span>0.00 m</span></div>
      <div class="row"><span>Slope</span><span>0.0158636°</span></div>
      <div class="row"><span>Slope as percentage</span><span class="box"></span></div>
    </div>

    <div class="photo" role="img" aria-label="Vue aérienne d'un chantier avec ligne de profil" style="left:120px;top:682px;width:166px;height:46px;background:linear-gradient(135deg,#8a8070,#bdb6a6)"></div>
    <svg class="abs" style="left:120px;top:730px" width="166" height="92" viewBox="0 0 166 92" aria-label="Profil d'élévation">
      <rect width="166" height="92" fill="#fff"/>
      <g stroke="#eee" stroke-width="1">
        <line x1="8" y1="15" x2="162" y2="15"/><line x1="8" y1="35" x2="162" y2="35"/>
        <line x1="8" y1="55" x2="162" y2="55"/><line x1="8" y1="75" x2="162" y2="75"/>
      </g>
      <path d="M8 75 L38 70 C52 60 57 24 72 20 L102 20 C116 24 122 60 134 70 L162 75 L162 80 L8 80 Z" fill="var(--chart-fill)"/>
      <path d="M8 75 L38 70 C52 60 57 24 72 20 L102 20 C116 24 122 60 134 70 L162 75" fill="none" stroke="var(--chart)" stroke-width="1.4"/>
    </svg>

    <div class="measure" style="left:290px;width:98px">
      <h4>Measurements</h4>
      <div class="row"><span>2D length</span><span>7.72 m</span></div>
      <div class="row"><span>3D length</span><span>7.72 m</span></div>
      <div class="row"><span>Min. elevation</span><span>675.27 m</span></div>
      <div class="row"><span>Max. elevation</span><span>675.27 m</span></div>
      <div class="row"><span>Elevation difference</span><span>0.00 m</span></div>
      <div class="row"><span>Slope</span><span>0.0276872%</span></div>
      <div class="row"><span>Slope as percentage</span><span class="box on"></span></div>
    </div>
  </section>

</div>
</body>
</html>
```